2014 Programme

We need a brochure for some training courses we are providing.

All content is available: http://tandrovix.com/academy/tandrovix-academy-programmes-2014

The brochure should be delivered in PDF and will be printed at a later date.

```html
<!DOCTYPE html>
<html lang="en">
<head>
<meta charset="utf-8">
<title>Building Bold Ventures – 2014 Programme</title>
<link href="https://fonts.googleapis.com/css2?family=Figtree:wght@300;400;600;700&display=swap" rel="stylesheet">
<style>
  :root {
    --navy: #04324d;
    --pink: #e4458e;
    --white: #ffffff;
    --ink: #5a5a5a;
    --ink-strong: #444444;
    --curve: #7fb3c2;
  }
  * { margin: 0; padding: 0; box-sizing: border-box; }
  html, body { width: 1200px; height: 841px; overflow: hidden; }
  body {
    position: relative;
    background: var(--white);
    font-family: "Figtree", "Helvetica Neue", Arial, sans-serif;
  }
  .spread-page { position: absolute; top: 0; height: 841px; }
  .page-overview { left: 0; width: 595px; background: var(--navy); color: var(--white); }
  .page-curriculum { left: 595px; width: 605px; background: var(--white); color: var(--ink); }

  .page-title {
    position: absolute; top: 36px;
    font-weight: 400; font-size: 46px; line-height: 1;
    color: var(--pink); letter-spacing: 0.3px;
  }
  .page-overview .page-title { left: 34px; }
  .page-curriculum .page-title { left: 35px; }

  .curriculum-intro {
    position: absolute; left: 35px; top: 95px;
    font-size: 13.5px; line-height: 17px; text-transform: uppercase;
    color: var(--ink); font-weight: 400;
  }

  .pull-quote {
    position: absolute; left: 35px; top: 184px; width: 165px;
    font-size: 16.5px; line-height: 22.5px; text-transform: uppercase; font-weight: 400;
  }
  .quote-author {
    position: absolute; left: 36px; top: 255px;
    font-size: 9.5px; color: #d0dbe2;
  }

  .growth-chart { position: absolute; left: 30px; top: 292px; }
  .growth-chart text { fill: var(--white); font-family: "Figtree", sans-serif; }

  .overview-body {
    position: absolute; left: 214px; top: 184px; width: 335px;
    font-size: 11.4px; line-height: 15.6px; font-weight: 400;
  }
  .overview-body p { margin-bottom: 15.6px; }
  .overview-body strong { font-weight: 700; }

  .course { position: absolute; left: 35px; width: 560px; }
  .course-part1 { top: 185px; }
  .course-part2 { top: 471px; }
  .course-label { position: absolute; left: 0; width: 170px; color: var(--pink); font-size: 11.6px; line-height: 16px; }
  .course-label .series { font-weight: 400; display: block; }
  .course-label .part { font-weight: 700; display: block; text-transform: uppercase; }
  .course-detail {
    position: absolute; left: 178px; width: 350px;
    font-size: 10.5px; line-height: 15px; color: var(--ink);
    letter-spacing: -0.05px;
  }
  .course-detail p { margin-bottom: 15px; }
  .topic-list { list-style: none; margin-bottom: 15px; }
  .topic-list li { padding-left: 8px; text-indent: -8px; }
  .topic-list li::before { content: "• "; }
  .topic-list strong { font-weight: 700; color: var(--ink-strong); }
</style>
</head>
<body>

<section class="spread-page page-overview">
  <h1 class="page-title">WORKSHOP OVERVIEW</h1>

  <blockquote class="pull-quote">“A STARTUP IS NOT A SMALL VERSION OF A BIG COMPANY”</blockquote>
  <p class="quote-author">Stan Whitlow</p>

  <svg class="growth-chart" width="175" height="130" viewBox="0 0 175 130" aria-label="Growth curve: what happens here?">
    <text x="3" y="12" font-size="10">$</text>
    <line x1="9" y1="18" x2="9" y2="116" stroke="#9fb4c1" stroke-width="1"/>
    <line x1="9" y1="116" x2="160" y2="116" stroke="#9fb4c1" stroke-width="1"/>
    <text x="162" y="121" font-size="10">t</text>
    <path d="M9 108 L120 107 C140 106 150 95 160 20" fill="none" stroke="var(--curve)" stroke-width="1.2"/>
    <text x="66" y="54" font-size="11" text-anchor="middle">WHAT</text>
    <text x="66" y="69" font-size="11" text-anchor="middle">HAPPENS</text>
    <text x="66" y="84" font-size="11" text-anchor="middle">HERE?</text>
  </svg>

  <div class="overview-body">
    <p>Most new products fail to get traction because they fail to learn what customers want. Over the past 10 years, a new discipline has emerged from the world of startups which can help.<br>
    Built upon lean manufacturing approaches, Lean Startup is a way for a new business to unlock customer value, faster and smarter than the competition.</p>
    <p><strong>Building Bold Ventures</strong> is a series of hands-on practical workshops which bring together some of the latest research and thinking with tools, stories and approaches.</p>
    <p>The course is designed for people whose job it is to turn ideas into new businesses. Each part takes 10-20 people from across the business (including group heads, product managers, engineers, designers) through 2 days of intense (but inspiring) work.</p>
    <p>Tandrovix is a 5 year old venture builder which has founded over 20 startups in Asia Pacific and this training has emerged from this work. This is entrepreneur- driven innovation practice that can revitalise how your company works and thinks. The know-how has already been shared with some of Asia Pacific’s biggest companies.</p>
  </div>
</section>

<section class="spread-page page-curriculum">
  <h2 class="page-title">A Two Part Curriculum</h2>
  <p class="curriculum-intro">We run two courses, each for a business<br>at a different stage in it’s life-cycle.</p>

  <article class="course course-part1">
    <h3 class="course-label"><span class="series">Building Bold Ventures:</span><span class="part">Part 1</span><span class="part">Problem Solution Fit</span></h3>
    <div class="course-detail">
      <p>This is focused on the first moment of inception as we try to understand how we can solve an actual problem for a real customer with a specific solution.</p>
      <ul class="topic-list">
        <li><strong>What is a startup?</strong> The Startup Blueprint and why startups fail</li>
        <li><strong>Introduction to Lean Startup:</strong> build, measure, learn</li>
        <li><strong>Venture Canvas:</strong> the business plan for the lean startup</li>
        <li><strong>Focus:</strong> because an unfocused hypothesis is impossible to test</li>
        <li><strong>Innovation Accounting:</strong> startup metrics</li>
        <li><strong>How to design and run experiments</strong></li>
        <li><strong>Manual testing and the ‘Wizard of Oz’ technique as tools<br>for customer development</strong></li>
        <li><strong>Lean Pitching Hacks</strong></li>
      </ul>
      <p>By the end of the two days, participants understand lean startup principles, have built and pivoted their business model, released a real product to customers (run an experiment) and pitched the business 3 times.</p>
    </div>
  </article>

  <article class="course course-part2">
    <h3 class="course-label"><span class="series">Building Bold Ventures:</span><span class="part">Part 2</span><span class="part">Product Market Fit</span></h3>
    <div class="course-detail">
      <p>This is focused on businesses that are a few months old, already with problem solution fit, now trying to understand how to build a product that a market wants with a sustainable business model. BBV 1 is a pre-requisite for this course.</p>
      <ul class="topic-list">
        <li><strong>Confirming that we have ‘problem solution fit’</strong> - what does it look like?</li>
        <li><strong>Lean Pitching Hacks Part 2</strong></li>
        <li><strong>Communicating traction.</strong> Manufacturing forward motion<br>and communicating with investors. Monthly updates and Backer Roll</li>
        <li><strong>What is ‘product market fit’?</strong> Systematically working through<br>the ‘Trough of sorrow’ to success</li>
        <li><strong>Lean Marketing.</strong> Practical growth hacking techniques and best<br>practice customer development</li>
        <li><strong>Innovation Accounting:</strong> startup metrics</li>
      </ul>
      <p>By the end of the two days, participants will have strengthened their application of lean startup, tightened their pitch and have a plan to the first 100,000 users with a few experiments already deployed in the market.</p>
    </div>
  </article>
</section>

</body>
</html>
```